Keystone Prime Water Tank

I primarily market the water tanks so want a business care that reflects that. I have attached the water tank logo. You have been working on our water tank so maybe we can use that on the card et. I am leaving as one sided but can be double sided if that works. The information that needs to be on the cards is as follows: Gerald T. Munro Phone numbers: Office 555-284-9137 Direct 555-619-2405 Mobile 555-372-5841 email address: gerald@fieldgearworks.com Address P.O. Box 8273 Ridgecliff, GA 30512 Web Page: www.fieldgearworks.com. A lot to fit on the card. Thanks

```html
<!DOCTYPE html>
<html lang="en">
<head>
<meta charset="utf-8">
<title>Keystone Prime Water Tank – Business Card</title>
<link rel="stylesheet" href="https://fonts.googleapis.com/css2?family=Open+Sans:wght@400;600;700&display=swap">
<style>
  :root {
    --backdrop: #3b3b3b;
    --card: #161616;
    --red: #e8232a;
    --white: #f2f2f2;
    --gloss: #2b2b2b;
  }
  * { box-sizing: border-box; margin: 0; padding: 0; }
  html, body {
    width: 1200px; height: 801px; overflow: hidden;
    background: var(--backdrop);
    font-family: "Open Sans", Arial, sans-serif;
  }
  .stage {
    width: 1200px; height: 801px;
    display: flex; align-items: center; justify-content: center; gap: 60px;
  }
  .card {
    position: relative;
    width: 520px; height: 297px;
    background: var(--card);
    border: 2px solid var(--red);
    border-radius: 3px;
  }
  /* Front */
  .brand {
    position: absolute; top: 36px; right: 36px;
    display: flex; align-items: center; gap: 10px;
  }
  .brand-square { width: 26px; height: 26px; background: var(--red); }
  .brand-name {
    color: var(--white); font-weight: 700; font-size: 17px;
    letter-spacing: 0.02em; text-transform: uppercase;
  }
  .holder {
    position: absolute; left: 36px; top: 104px;
    color: var(--red); font-weight: 700; font-size: 20px;
  }
  .divider {
    position: absolute; left: 36px; right: 36px; top: 140px;
    height: 1px; background: var(--red);
  }
  .contacts {
    position: absolute; left: 36px; top: 156px;
    list-style: none; color: var(--white); font-size: 13px; line-height: 22px;
  }
  .contacts li { display: flex; align-items: center; gap: 9px; }
  .contacts svg { width: 12px; height: 12px; fill: var(--red); flex: none; }
  .contacts .label { color: var(--red); font-size: 11px; margin-left: 4px; }
  .address {
    position: absolute; right: 36px; top: 156px;
    color: var(--white); font-size: 13px; line-height: 20px; text-align: right;
    font-style: normal;
  }
  /* Back */
  .back { display: flex; align-items: center; justify-content: center; gap: 14px; }
  .back .brand-square { width: 40px; height: 40px; background: var(--gloss); }
  .back .brand-name { color: var(--gloss); font-size: 26px; }
</style>
</head>
<body>
<main class="stage">
  <section class="card front">
    <div class="brand">
      <span class="brand-square"></span>
      <span class="brand-name">Keystone Prime Water Tank</span>
    </div>
    <h1 class="holder">Gerald T. Munro</h1>
    <div class="divider"></div>
    <ul class="contacts">
      <li><svg viewBox="0 0 24 24"><path d="M6.6 10.8a15 15 0 0 0 6.6 6.6l2.2-2.2c.3-.3.7-.4 1-.2 1.1.4 2.3.6 3.6.6.6 0 1 .4 1 1V20c0 .6-.4 1-1 1A17 17 0 0 1 3 4c0-.6.4-1 1-1h3.5c.6 0 1 .4 1 1 0 1.3.2 2.5.6 3.6.1.3 0 .7-.2 1z"/></svg>555-284-9137<span class="label">Office</span></li>
      <li><svg viewBox="0 0 24 24"><path d="M6.6 10.8a15 15 0 0 0 6.6 6.6l2.2-2.2c.3-.3.7-.4 1-.2 1.1.4 2.3.6 3.6.6.6 0 1 .4 1 1V20c0 .6-.4 1-1 1A17 17 0 0 1 3 4c0-.6.4-1 1-1h3.5c.6 0 1 .4 1 1 0 1.3.2 2.5.6 3.6.1.3 0 .7-.2 1z"/></svg>555-619-2405<span class="label">Direct</span></li>
      <li><svg viewBox="0 0 24 24"><path d="M7 1h10a2 2 0 0 1 2 2v18a2 2 0 0 1-2 2H7a2 2 0 0 1-2-2V3a2 2 0 0 1 2-2zm0 3v14h10V4z"/></svg>555-372-5841<span class="label">Mobile</span></li>
      <li><svg viewBox="0 0 24 24"><path d="M2 5h20v14H2zm2 2v.5l8 5 8-5V7z"/></svg>gerald@fieldgearworks.com</li>
      <li><svg viewBox="0 0 24 24"><circle cx="12" cy="12" r="10"/></svg>www.fieldgearworks.com</li>
    </ul>
    <address class="address">P.O. Box 8273<br>Ridgecliff, GA 30512</address>
  </section>

  <section class="card back">
    <span class="brand-square"></span>
    <span class="brand-name">Keystone Prime Water Tank</span>
  </section>
</main>
</body>
</html>
```